Graphic to communicate emotional connection

Howdy-I need a graphic that describe my financial planning process.The attached is a concept, but please use your own creativity to show how you would display this:- The four circles on the outside (Protect what we have, know where it goes, make it grow, and dignity and independence) are the four major areas of concern- Then, there are three value statements:- The first is the most powerful which is that Clarity leads to Control which allows your Intentions to come through- The second shows that we take our clients from Uncertainty and Confusion, to Confidence and Intention- The third says we create space for you to develop your Purposeful Effort which leads to Your Best Financial Life.I've also attached my logo - please use the colors in my logo and maybe add a soft green as needed.The reader should be able to briefly scan this document and understand that we will connect with them on an emotional level to get their finances in shape.Thanks!-Ned

Target Market(s)

wealthy women, whether independent or married

Industry/Entity Type

Financial Planning

Requirements
Must have
• Please use the colors in my logo plus a soft green as needed
Should not have
• This should not be a busy or hard-to-read graphic. It is meant to convey an that I try to make an emotional connection, at a glance.

```html
<!DOCTYPE html>
<html lang="en">
<head>
<meta charset="utf-8">
<title>Our Aspiration</title>
<link rel="stylesheet" href="https://fonts.googleapis.com/css2?family=Oswald:wght@500;600;700&family=Open+Sans:wght@400;600&display=swap">
<style>
  :root {
    --navy: #1f3f86;
    --blue: #2b55a1;
    --ink: #111111;
    --stone: #8a8788;
    --band-dark: #cfc9cb;
    --band-light: #f3f1f2;
    --frame: #dcd7d9;
    --pill-dark: #dedbdc;
    --pill-light: #fbfbfb;
    --paper: #ffffff;
  }
  html, body {
    margin: 0;
    padding: 0;
    width: 1200px;
    height: 720px;
    overflow: hidden;
    background: var(--paper);
  }
  .aspiration {
    display: block;
    width: 1200px;
    height: 720px;
  }
  .title {
    font-family: "Oswald", sans-serif;
    font-weight: 700;
    font-size: 46px;
    fill: var(--ink);
  }
  .step-label {
    font-family: "Open Sans", sans-serif;
    font-size: 16px;
    fill: var(--paper);
  }
  .concern-label {
    font-family: "Oswald", sans-serif;
    font-weight: 600;
    font-size: 15px;
    fill: var(--ink);
  }
  .node-label {
    font-family: "Open Sans", sans-serif;
    font-weight: 600;
    font-size: 12.5px;
    fill: var(--ink);
  }
  .state-from {
    font-family: "Oswald", sans-serif;
    font-weight: 600;
    font-size: 19px;
    fill: var(--stone);
  }
  .state-to {
    font-family: "Oswald", sans-serif;
    font-weight: 600;
    font-size: 19px;
    fill: var(--navy);
  }
  .step-arrow { fill: var(--navy); }
  .title-rule { fill: var(--stone); }
  .frame { fill: var(--paper); stroke: url(#frameGrad); stroke-width: 10; }
  .ring { fill: var(--paper); stroke: var(--navy); stroke-width: 7; }
  .concern-ring { fill: var(--paper); stroke: var(--navy); stroke-width: 8; }
  .concern-tab { fill: var(--blue); }
  .concern-pill { fill: url(#pillGrad); stroke: #e9e7e8; stroke-width: 1.5; }
  .band { fill: url(#bandGrad); }
  .band-divider { stroke: var(--paper); stroke-width: 2; }
</style>
</head>
<body>
<svg class="aspiration" viewBox="0 0 1000 600" xmlns="http://www.w3.org/2000/svg">
  <defs>
    <linearGradient id="bandGrad" x1="0" y1="0" x2="1" y2="0">
      <stop offset="0" stop-color="var(--band-dark)"/>
      <stop offset="1" stop-color="var(--band-light)"/>
    </linearGradient>
    <linearGradient id="pillGrad" x1="0" y1="0" x2="0" y2="1">
      <stop offset="0" stop-color="var(--pill-light)"/>
      <stop offset="1" stop-color="var(--pill-dark)"/>
    </linearGradient>
    <linearGradient id="frameGrad" x1="0" y1="0" x2="1" y2="0">
      <stop offset="0" stop-color="#c9c3c5"/>
      <stop offset="1" stop-color="#ebe8e9"/>
    </linearGradient>
  </defs>

  <!-- heading -->
  <text class="title" x="495" y="70" text-anchor="middle">OUR ASPIRATION</text>
  <rect class="title-rule" x="348" y="80" width="298" height="3"/>

  <!-- process steps -->
  <g class="steps">
    <polygon class="step-arrow" points="253,121 410,121 428,138.5 410,156 253,156 271,138.5"/>
    <polygon class="step-arrow" points="418,121 575,121 593,138.5 575,156 418,156 436,138.5"/>
    <polygon class="step-arrow" points="583,121 742,121 760,138.5 742,156 583,156 601,138.5"/>
    <text class="step-label" x="338" y="144" text-anchor="middle">Clarity</text>
    <text class="step-label" x="505" y="144" text-anchor="middle">Control</text>
    <text class="step-label" x="672" y="144" text-anchor="middle">Intention</text>
  </g>

  <!-- central frame -->
  <rect class="frame" x="227" y="172" width="566" height="324" rx="28"/>

  <!-- areas of concern -->
  <g class="concern concern-protect">
    <polygon class="concern-tab" points="215,193 243,193 256,209 243,225 215,225"/>
    <circle class="concern-ring" cx="205" cy="209" r="34"/>
    <rect class="concern-pill" x="48" y="181" width="166" height="56" rx="28"/>
    <text class="concern-label" x="128" y="206" text-anchor="middle">PROTECT WHAT</text>
    <text class="concern-label" x="128" y="225" text-anchor="middle">WE HAVE</text>
  </g>
  <g class="concern concern-grow">
    <polygon class="concern-tab" points="215,433 243,433 256,449 243,465 215,465"/>
    <circle class="concern-ring" cx="205" cy="449" r="34"/>
    <rect class="concern-pill" x="48" y="421" width="166" height="56" rx="28"/>
    <text class="concern-label" x="128" y="446" text-anchor="middle">MAKE IT</text>
    <text class="concern-label" x="128" y="465" text-anchor="middle">GROW</text>
  </g>
  <g class="concern concern-track">
    <polygon class="concern-tab" points="785,203 757,203 744,219 757,235 785,235"/>
    <circle class="concern-ring" cx="808" cy="219" r="34"/>
    <rect class="concern-pill" x="800" y="191" width="164" height="56" rx="28"/>
    <text class="concern-label" x="882" y="215" text-anchor="middle">KNOW WHERE</text>
    <text class="concern-label" x="882" y="234" text-anchor="middle">IT GOES</text>
  </g>
  <g class="concern concern-dignity">
    <polygon class="concern-tab" points="785,440 757,440 744,456 757,472 785,472"/>
    <circle class="concern-ring" cx="808" cy="456" r="34"/>
    <rect class="concern-pill" x="800" y="428" width="164" height="56" rx="28"/>
    <text class="concern-label" x="882" y="452" text-anchor="middle">DIGNITY &amp;</text>
    <text class="concern-label" x="882" y="471" text-anchor="middle">INDEPENDENCE</text>
  </g>

  <!-- statement: from uncertainty to confidence -->
  <g class="statement statement-shift">
    <polygon class="band" points="330,208 478,208 500,254 478,300 330,300"/>
    <line class="band-divider" x1="370" y1="254" x2="490" y2="254"/>
    <text class="state-from" x="427" y="245" text-anchor="middle">UNCERTAINTY</text>
    <text class="state-from" x="419" y="279" text-anchor="middle">CONFUSION</text>
    <circle class="ring" cx="318" cy="254" r="40"/>
    <text class="node-label" x="318" y="250" text-anchor="middle">We take</text>
    <text class="node-label" x="318" y="266" text-anchor="middle">you from</text>

    <polygon class="band" points="570,208 718,208 740,254 718,300 570,300"/>
    <line class="band-divider" x1="600" y1="254" x2="730" y2="254"/>
    <text class="state-to" x="663" y="245" text-anchor="middle">CONFIDENCE</text>
    <text class="state-to" x="660" y="279" text-anchor="middle">INTENTION</text>
    <circle class="ring" cx="557" cy="254" r="40"/>
    <text class="node-label" x="557" y="258" text-anchor="middle">To</text>
  </g>

  <!-- statement: purposeful effort to best financial life -->
  <g class="statement statement-effort">
    <polygon class="band" points="330,360 478,360 500,407 478,454 330,454"/>
    <text class="state-from" x="422" y="401" text-anchor="middle">PURPOSEFUL</text>
    <text class="state-from" x="422" y="423" text-anchor="middle">EFFORT</text>
    <circle class="ring" cx="313" cy="407" r="40"/>
    <text class="node-label" x="313" y="388" text-anchor="middle">We</text>
    <text class="node-label" x="313" y="403" text-anchor="middle">create</text>
    <text class="node-label" x="313" y="418" text-anchor="middle">space for</text>
    <text class="node-label" x="313" y="433" text-anchor="middle">you</text>

    <polygon class="band" points="575,360 723,360 745,407 723,454 575,454"/>
    <text class="state-to" x="660" y="390" text-anchor="middle">BEST</text>
    <text class="state-to" x="660" y="413" text-anchor="middle">FINANCIAL</text>
    <text class="state-to" x="660" y="436" text-anchor="middle">LIFE</text>
    <circle class="ring" cx="563" cy="407" r="40"/>
    <text class="node-label" x="563" y="403" text-anchor="middle">Which</text>
    <text class="node-label" x="563" y="419" text-anchor="middle">leads to</text>
  </g>
</svg>
</body>
</html>
```